Health care technology software systems

We have a solid logo. We have company colors that will need to be used as well. We just need a great business card design. We sell to health plans but want to be modern
Updates

Need extra days to review

Target Market(s)

Health technology sector selling into Health Plans

Industry/Entity Type

Health Care Technology

Contact Information for Business Card

Name, title, address, phone number, email

Requirements
Must have
• Use of Kembrata corporate colors - Uploaded w/ our logos

```html
<!DOCTYPE html>
<html lang="en">
<head>
<meta charset="utf-8">
<title>Kembrata Business Card</title>
<link href="https://fonts.googleapis.com/css2?family=Montserrat:wght@300;400;500&display=swap" rel="stylesheet">
<style>
  :root {
    --backdrop: #d2cdd0;
    --card-dark: #393a37;
    --card-light: #ffffff;
    --ink: #2f302e;
    --brand-green: #8dc63f;
    --brand-blue: #29abe2;
    --brand-navy: #3b55a5;
    --white: #ffffff;
  }
  html, body {
    margin: 0;
    padding: 0;
    width: 1200px;
    height: 1200px;
    overflow: hidden;
    background: var(--backdrop);
    font-family: "Montserrat", Arial, sans-serif;
  }
  .canvas {
    position: relative;
    width: 1200px;
    height: 1200px;
  }
  .card {
    position: absolute;
    left: 180px;
    width: 814px;
    height: 464px;
    overflow: hidden;
    box-shadow: 0 2px 6px rgba(0,0,0,0.18);
  }
  .card-front { top: 98px; background: var(--card-dark); }
  .card-back { top: 624px; height: 466px; background: var(--card-light); }

  .accent-field {
    position: absolute;
    width: 100px;
    background: linear-gradient(90deg, var(--brand-green) 0%, var(--brand-blue) 50%, var(--brand-navy) 100%);
    border-radius: 4px;
  }
  .front-accent {
    left: 682px;
    top: 0;
    height: 340px;
    opacity: 0.55;
    -webkit-mask-image: linear-gradient(180deg, #000 55%, transparent 100%);
    mask-image: linear-gradient(180deg, #000 55%, transparent 100%);
  }
  .back-accent {
    left: 660px;
    top: 126px;
    height: 340px;
    opacity: 0.4;
    -webkit-mask-image: linear-gradient(0deg, #000 55%, transparent 100%);
    mask-image: linear-gradient(0deg, #000 55%, transparent 100%);
  }

  .brand-mark {
    position: absolute;
    border-radius: 50%;
    background: var(--brand-green);
  }
  .front-mark { left: 330px; top: 96px; width: 156px; height: 156px; }
  .back-mark { left: 374px; top: 44px; width: 72px; height: 72px; }

  .brand-name {
    position: absolute;
    margin: 0;
    font-weight: 300;
    line-height: 1;
    letter-spacing: 1px;
  }
  .front-name {
    left: 0;
    width: 814px;
    top: 286px;
    text-align: center;
    font-size: 92px;
    color: var(--white);
  }
  .back-name {
    left: 470px;
    top: 50px;
    font-size: 62px;
    color: var(--ink);
  }

  .holder-name {
    position: absolute;
    left: 58px;
    top: 150px;
    margin: 0;
    font-size: 24px;
    font-weight: 500;
    letter-spacing: 2px;
    color: var(--ink);
    line-height: 1;
  }
  .holder-title {
    position: absolute;
    left: 58px;
    top: 184px;
    margin: 0;
    font-size: 21px;
    font-weight: 400;
    letter-spacing: 1px;
    color: var(--brand-green);
    line-height: 1;
  }
  .divider {
    position: absolute;
    left: 58px;
    top: 219px;
    width: 594px;
    height: 2px;
    background: var(--brand-green);
  }
  .address {
    position: absolute;
    left: 58px;
    top: 250px;
    margin: 0;
    font-size: 17px;
    letter-spacing: 1.5px;
    line-height: 22px;
    color: var(--ink);
    font-style: normal;
  }
  .contact-row {
    position: absolute;
    left: 64px;
    display: flex;
    align-items: center;
    font-size: 17px;
    letter-spacing: 1px;
    color: var(--ink);
  }
  .contact-row svg { width: 20px; height: 20px; margin-right: 24px; }
  .contact-phone { top: 336px; }
  .contact-email { top: 372px; }
</style>
</head>
<body>
<main class="canvas">

  <section class="card card-front" aria-label="Card front">
    <div class="accent-field front-accent" role="img" aria-label="Glowing light lines and dots in green, blue and navy"></div>
    <div class="brand-mark front-mark" aria-hidden="true"></div>
    <p class="brand-name front-name">kembrata</p>
  </section>

  <section class="card card-back" aria-label="Card back">
    <div class="accent-field back-accent" role="img" aria-label="Rising dots and glowing light lines in green, blue and navy"></div>

    <div class="brand-mark back-mark" aria-hidden="true"></div>
    <p class="brand-name back-name">kembrata</p>

    <h1 class="holder-name">Your Name:</h1>
    <p class="holder-title">Title</p>
    <div class="divider"></div>
    <address class="address">Street Loation,<br>state,country.</address>

    <div class="contact-row contact-phone">
      <svg viewBox="0 0 24 24" aria-hidden="true"><path fill="var(--brand-green)" d="M6.6 10.8a15.1 15.1 0 0 0 6.6 6.6l2.2-2.2a1 1 0 0 1 1-.25 11.4 11.4 0 0 0 3.6.57 1 1 0 0 1 1 1V20a1 1 0 0 1-1 1A17 17 0 0 1 3 4a1 1 0 0 1 1-1h3.5a1 1 0 0 1 1 1c0 1.25.2 2.45.57 3.57a1 1 0 0 1-.25 1z"/></svg>
      <span>01+2345 6789 0123</span>
    </div>
    <div class="contact-row contact-email">
      <svg viewBox="0 0 24 24" aria-hidden="true"><rect x="2" y="5" width="20" height="14" fill="var(--brand-green)"/><path d="M2.5 5.5 12 13l9.5-7.5" fill="none" stroke="#ffffff" stroke-width="1.6"/></svg>
      <span>info@company.com</span>
    </div>
  </section>

</main>
</body>
</html>
```